tilebarnowl.net needs a cool website!

I need a website designed for a commercial flooring maintenance company based in Texas. We will be providing services like carpet shampooing, burnishing, resurfacing and power washing. It needs to be cool and trendy.

I’ll need 10-20 pages. I need help deciding on the style and color palette. We will need great stock pictures of different flooring types and you will need to photo shop our logo on imaginary cars or storefronts.

Please have similar experience and an open mind. I’m looking for a partnership and someone to turn to for future projects and upkeep.

The domain is currently hosted on Wix. You will need the ability to develop and code it there.

Target Market(s)

Commercial businesses and properties

Industry/Entity Type

Floor care

Coding

Coded - Design and coding required

Number of Pages Required

5+ page

Requirements
Must have
• Great pictures of different types of floors.

```html
<!DOCTYPE html>
<html lang="en">
<head>
<meta charset="utf-8">
<title>tilebarnowl.net – Commercial Floor Care</title>
<link rel="stylesheet" href="https://fonts.googleapis.com/css2?family=Montserrat:wght@300;400;500;600&family=Lato:wght@400;700&display=swap">
<style>
:root{
  --green:#7fa83a;
  --green-dark:#6c9230;
  --ink:#1e1e1e;
  --text:#555;
  --muted:#8a8a8a;
  --line:#d9d9d9;
  --soft:#f3f4f1;
  --black:#000;
  --white:#fff;
}
*{box-sizing:border-box;margin:0;padding:0}
html,body{width:1200px;height:4399px;overflow:hidden}
body{position:relative;background:var(--white);font-family:"Lato",sans-serif;color:var(--text)}
.abs{position:absolute}
.btn{position:absolute;display:flex;align-items:center;justify-content:center;gap:7px;background:var(--green);color:var(--white);font:700 13px "Lato",sans-serif;text-transform:uppercase;letter-spacing:.2px}
.btn svg{width:10px;height:10px}
.brand{font:400 34px "Montserrat",sans-serif;color:var(--ink);display:flex;align-items:center;gap:10px}
.brand i{display:block;width:30px;height:30px;border-radius:50%;background:var(--ink)}
.section-title{position:absolute;left:0;width:1200px;text-align:center;font:400 30px "Montserrat",sans-serif;color:var(--ink);text-transform:uppercase}
.section-title span,.about-title span{color:var(--green)}
.photo{position:absolute}

/* header */
.site-header{position:absolute;left:0;top:0;width:1200px;height:100px;background:var(--white)}
.nav{position:absolute;top:44px;font:400 13px "Montserrat",sans-serif;color:var(--ink);text-transform:uppercase}
.nav.active{color:var(--green)}

/* hero */
.hero{position:absolute;left:0;top:100px;width:1200px;height:498px;background:linear-gradient(180deg,#8d9aa6 0%,#c9c2b8 35%,#6c7680 58%,#59616a 100%)}
.hero-title{position:absolute;left:0;width:1200px;text-align:center;top:250px;font:300 46px "Montserrat",sans-serif;color:var(--white);letter-spacing:.5px}
.hero-sub{position:absolute;left:0;width:1200px;text-align:center;top:310px;font:500 37px "Montserrat",sans-serif;color:var(--white)}
.arrow{position:absolute;width:24px;height:24px}
.badge{position:absolute;left:842px;top:75px;width:132px;height:132px}

/* about */
.about{position:absolute;left:0;top:598px;width:1200px;height:634px;background:linear-gradient(90deg,#fff 40%,#f4f7ee 100%)}
.about-block{position:absolute;left:111px;top:0;width:341px;height:597px;background:var(--soft)}
.about-title{position:absolute;left:708px;top:184px;font:400 31px "Montserrat",sans-serif;color:var(--ink)}
.body-copy{font:400 13px/26px "Lato",sans-serif;color:var(--text)}

/* services */
.services{position:absolute;left:0;top:1232px;width:1200px;height:632px;background:linear-gradient(180deg,#f3f4f6,#f9faf8)}
.lead{position:absolute;left:0;width:1200px;text-align:center;font:400 13px/26px "Lato",sans-serif;color:var(--text)}
.service{position:absolute;top:407px;width:278px;border-left:2px solid var(--green);padding-left:21px;height:128px}
.service h3{font:700 14px "Lato",sans-serif;color:var(--ink);margin-top:6px;text-transform:uppercase}
.service p{font:400 13px/24px "Lato",sans-serif;color:var(--text);margin-top:8px}
.more{display:flex;align-items:center;gap:5px;font:700 13px "Lato",sans-serif;color:var(--green);text-transform:uppercase;margin-top:4px}
.more svg{width:10px;height:10px}

/* cta */
.cta{position:absolute;left:0;top:1864px;width:1200px;height:376px;background:var(--green)}
.cta h2{position:absolute;left:111px;top:82px;font:400 31px "Montserrat",sans-serif;color:var(--white);z-index:2}
.cta p{position:absolute;left:114px;top:136px;width:500px;font:400 13px/26px "Lato",sans-serif;color:var(--white);z-index:2}
.cta .btn{background:var(--white);color:var(--ink)}
.van{left:650px;top:1975px;width:550px;height:385px;border-radius:110px 0 60px 80px;background:linear-gradient(180deg,#f4f5f6 0%,#dfe2e5 60%,#6c6f73 100%)}

/* testimonials */
.card{position:absolute;top:2485px;width:304px;height:203px;background:var(--white);box-shadow:0 4px 22px rgba(0,0,0,.08)}
.avatar{position:absolute;left:37px;top:-26px;width:76px;height:76px;border-radius:50%;background:radial-gradient(circle at 50% 45%,#5b6b7a,#1f2a36)}
.company{position:absolute;left:155px;top:44px;font:400 14px "Lato",sans-serif;color:var(--text)}
.person{position:absolute;left:31px;top:68px;font:400 17px "Lato",sans-serif;color:var(--ink)}
.stars{position:absolute;left:164px;top:68px;display:flex;gap:2px}
.stars svg{width:14px;height:14px}
.card p{position:absolute;left:31px;top:101px;width:250px;font:400 12.5px/24px "Lato",sans-serif;color:var(--text)}
.card a{position:absolute;left:198px;top:152px;font:400 11px "Lato",sans-serif;color:var(--green);text-decoration:underline}

/* gallery */
.gallery{position:absolute;left:0;top:2782px;width:1200px;height:705px;background:linear-gradient(90deg,#f2f2f2,#f7f9f2)}

/* contact */
.info{position:absolute;top:3641px;display:flex;align-items:center;gap:16px}
.info .ico{width:52px;height:52px;border-radius:50%;background:var(--green);display:flex;align-items:center;justify-content:center}
.info .ico svg{width:20px;height:20px}
.info small{display:block;font:400 12px "Lato",sans-serif;color:var(--text)}
.info strong{display:block;font:700 17px "Lato",sans-serif;color:var(--ink);margin-top:6px}
.field{position:absolute;border:1px solid var(--line);background:var(--white);padding:17px 18px;font:400 11px "Lato",sans-serif;color:var(--text);text-transform:uppercase}

/* footer */
.site-footer{position:absolute;left:0;top:4032px;width:1200px;height:367px;background:var(--black)}
.foot-nav{position:absolute;left:0;width:1200px;top:174px;display:flex;justify-content:center;gap:24px;font:400 13px "Lato",sans-serif;color:var(--white)}
.social{position:absolute;top:226px;width:40px;height:40px;border-radius:50%;background:var(--white)}
.copy{position:absolute;left:0;width:1200px;top:302px;text-align:center;font:400 12px "Lato",sans-serif;color:var(--white)}
</style>
</head>
<body>

<!-- header -->
<header class="site-header">
  <div class="brand abs" style="left:111px;top:27px"><i></i>tilebarnowl.net</div>
  <span class="nav active" style="left:492px">Home</span>
  <span class="nav" style="left:565px">About</span>
  <span class="nav" style="left:637px">Services</span>
  <span class="nav" style="left:722px">Gallery</span>
  <span class="nav" style="left:806px">Testimonials</span>
  <span class="btn" style="left:937px;top:31px;width:150px;height:42px">Contact Us</span>
</header>

<!-- hero -->
<section class="hero" role="img" aria-label="City skyline at dusk behind a wide paved commercial plaza">
  <svg class="arrow" style="left:80px;top:202px" viewBox="0 0 24 24"><path d="M15 4 7 12l8 8" fill="none" stroke="#fff" stroke-width="3"/></svg>
  <svg class="arrow" style="left:1098px;top:202px" viewBox="0 0 24 24"><path d="M9 4l8 8-8 8" fill="none" stroke="#fff" stroke-width="3"/></svg>
  <svg class="badge" viewBox="0 0 132 132">
    <defs><path id="ring" d="M14 66a52 52 0 1 1 104 0"/></defs>
    <circle cx="66" cy="66" r="42" fill="#fff"/>
    <text font-family="Montserrat,sans-serif" font-size="14" fill="#fff"><textPath href="#ring" startOffset="4%">Serving Texas Businesses</textPath></text>
    <text x="66" y="56" text-anchor="middle" font-family="Lato,sans-serif" font-size="13" fill="#222">for over</text>
    <text x="66" y="84" text-anchor="middle" font-family="Montserrat,sans-serif" font-weight="600" font-size="28" fill="#7fa83a">10</text>
    <text x="66" y="102" text-anchor="middle" font-family="Lato,sans-serif" font-size="13" fill="#222">Years</text>
  </svg>
  <h1 class="hero-title">TRANSFORM YOUR COMMERCIAL SPACE</h1>
  <p class="hero-sub">with Expert Flooring Maintenance</p>
  <span class="btn" style="left:483px;top:381px;width:236px;height:46px">Request a Free Quote <svg viewBox="0 0 10 10"><path d="M1 5h7M5 1l4 4-4 4" fill="none" stroke="#fff" stroke-width="2"/></svg></span>
</section>

<!-- about -->
<section class="about">
  <div class="about-block"></div>
  <div class="photo" role="img" aria-label="Office interior with glass wall sign and city view" style="left:162px;top:124px;width:483px;height:292px;background:linear-gradient(135deg,#3a3e44,#6f7a86 55%,#2b2e33);box-shadow:0 8px 20px rgba(0,0,0,.25)"></div>
  <div class="photo" role="img" aria-label="Modern glass office building under blue sky" style="left:210px;top:360px;width:302px;height:182px;background:linear-gradient(180deg,#9fc8ef 0%,#4f86c4 55%,#7ca06a 100%);box-shadow:0 8px 20px rgba(0,0,0,.2)"></div>
  <h2 class="about-title">ABOUT <span>US</span></h2>
  <p class="body-copy abs" style="left:708px;top:240px;width:370px">Lorem ipsum dolor sit amet, consectetur adipiscing elit. Sed fermentum fringilla ipsum ac tincidunt. Curabitur viverra mauris et nisl ornare fermentum quis ut est. Suspendisse fringilla pretium urna ut sodales. Sed sit amet diam dictum, viverra erat vel, facilisis eros. Cras lacinia tincidunt neque, sit amet interdum arcu rutrum non.</p>
  <span class="btn" style="left:708px;top:424px;width:150px;height:43px">Learn More <svg viewBox="0 0 10 10"><path d="M1 5h7M5 1l4 4-4 4" fill="none" stroke="#fff" stroke-width="2"/></svg></span>
</section>

<!-- services -->
<section class="services">
  <h2 class="section-title" style="top:70px">OUR <span>SERVICES</span></h2>
  <p class="lead" style="top:119px">Lorem ipsum dolor sit amet, consectetur adipiscing elit. Sed fermentum fringilla<br>ipsum ac tincidunt. Curabitur viverra mauris et nisl</p>
  <svg class="arrow" style="left:79px;top:344px" viewBox="0 0 24 24"><path d="M15 4 7 12l8 8" fill="none" stroke="#333" stroke-width="3"/></svg>
  <svg class="arrow" style="left:1098px;top:344px" viewBox="0 0 24 24"><path d="M9 4l8 8-8 8" fill="none" stroke="#333" stroke-width="3"/></svg>

  <div class="photo" role="img" aria-label="Worker shampooing carpet in a commercial hall" style="left:135px;top:202px;width:278px;height:188px;background:linear-gradient(160deg,#7aa2c8,#2f4a68)"></div>
  <div class="photo" role="img" aria-label="Floor burnishing machine on a polished floor" style="left:461px;top:202px;width:278px;height:188px;background:linear-gradient(160deg,#d8a86a,#6b6e74 60%,#c7c9cc)"></div>
  <div class="photo" role="img" aria-label="Freshly resurfaced glossy hardwood floor" style="left:787px;top:202px;width:278px;height:188px;background:linear-gradient(170deg,#d9cbb5,#a8451e 60%,#6e2a10)"></div>

  <div class="service" style="left:135px">
    <h3>Carpet Shampooing</h3>
    <p>Lorem ipsum dolor sit amet, consectetur adipiscing elit. Sed fermentum fringilla ipsum ac tincidunt.</p>
    <span class="more">Learn More <svg viewBox="0 0 10 10"><path d="M1 5h7M5 1l4 4-4 4" fill="none" stroke="#7fa83a" stroke-width="2"/></svg></span>
  </div>
  <div class="service" style="left:461px">
    <h3>Burnishing</h3>
    <p>Lorem ipsum dolor sit amet, consectetur adipiscing elit. Sed fermentum fringilla ipsum ac tincidunt.</p>
    <span class="more">Learn More <svg viewBox="0 0 10 10"><path d="M1 5h7M5 1l4 4-4 4" fill="none" stroke="#7fa83a" stroke-width="2"/></svg></span>
  </div>
  <div class="service" style="left:787px">
    <h3>Resurfacing</h3>
    <p>Lorem ipsum dolor sit amet, consectetur adipiscing elit. Sed fermentum fringilla ipsum ac tincidunt.</p>
    <span class="more">Learn More <svg viewBox="0 0 10 10"><path d="M1 5h7M5 1l4 4-4 4" fill="none" stroke="#7fa83a" stroke-width="2"/></svg></span>
  </div>
</section>

<!-- call to action -->
<section class="cta">
  <h2>READY TO REVITALIZE YOUR FLOORS?”</h2>
  <p>Lorem ipsum dolor sit amet, consectetur adipiscing elit. Sed fermentum fringilla ipsum ac tincidunt. Curabitur viverra mauris et nisl ornare fermentum quis ut est. Suspendisse fringilla pretium urna ut sodales.</p>
  <span class="btn" style="left:114px;top:239px;width:268px;height:48px">Get a Free Estimate Today <svg viewBox="0 0 10 10"><path d="M1 5h7M5 1l4 4-4 4" fill="none" stroke="#1e1e1e" stroke-width="2"/></svg></span>
</section>
<div class="photo van" role="img" aria-label="White company service van with branding on its side"></div>

<!-- testimonials -->
<h2 class="section-title" style="top:2398px">OUR <span>TESTIMONIALS</span></h2>
<svg class="arrow" style="left:79px;top:2574px" viewBox="0 0 24 24"><path d="M15 4 7 12l8 8" fill="none" stroke="#333" stroke-width="3"/></svg>
<svg class="arrow" style="left:1098px;top:2574px" viewBox="0 0 24 24"><path d="M9 4l8 8-8 8" fill="none" stroke="#333" stroke-width="3"/></svg>

<div class="card" style="left:114px">
  <div class="avatar" role="img" aria-label="Client portrait"></div>
  <span class="company">Company Name</span>
  <span class="person">Jhon Smith</span>
  <span class="stars"><svg viewBox="0 0 10 10"><path d="M5 0l1.5 3.3 3.5.4-2.6 2.4.7 3.5L5 7.8 1.9 9.6l.7-3.5L0 3.7l3.5-.4z" fill="#e7641c"/></svg><svg viewBox="0 0 10 10"><path d="M5 0l1.5 3.3 3.5.4-2.6 2.4.7 3.5L5 7.8 1.9 9.6l.7-3.5L0 3.7l3.5-.4z" fill="#e7641c"/></svg><svg viewBox="0 0 10 10"><path d="M5 0l1.5 3.3 3.5.4-2.6 2.4.7 3.5L5 7.8 1.9 9.6l.7-3.5L0 3.7l3.5-.4z" fill="#e7641c"/></svg><svg viewBox="0 0 10 10"><path d="M5 0l1.5 3.3 3.5.4-2.6 2.4.7 3.5L5 7.8 1.9 9.6l.7-3.5L0 3.7l3.5-.4z" fill="#e7641c"/></svg><svg viewBox="0 0 10 10"><path d="M5 0l1.5 3.3 3.5.4-2.6 2.4.7 3.5L5 7.8 1.9 9.6l.7-3.5L0 3.7l3.5-.4z" fill="#e7641c"/></svg></span>
  <p>Lorem ipsum dolor sit amet, sectetur adipiscing elit. Sed fermentum fringilla ipsum ac tincidunt.</p>
  <a>Learn More</a>
</div>
<div class="card" style="left:449px">
  <div class="avatar" role="img" aria-label="Client portrait"></div>
  <span class="company">Company Name</span>
  <span class="person">Jhon Smith</span>
  <span class="stars"><svg viewBox="0 0 10 10"><path d="M5 0l1.5 3.3 3.5.4-2.6 2.4.7 3.5L5 7.8 1.9 9.6l.7-3.5L0 3.7l3.5-.4z" fill="#e7641c"/></svg><svg viewBox="0 0 10 10"><path d="M5 0l1.5 3.3 3.5.4-2.6 2.4.7 3.5L5 7.8 1.9 9.6l.7-3.5L0 3.7l3.5-.4z" fill="#e7641c"/></svg><svg viewBox="0 0 10 10"><path d="M5 0l1.5 3.3 3.5.4-2.6 2.4.7 3.5L5 7.8 1.9 9.6l.7-3.5L0 3.7l3.5-.4z" fill="#e7641c"/></svg><svg viewBox="0 0 10 10"><path d="M5 0l1.5 3.3 3.5.4-2.6 2.4.7 3.5L5 7.8 1.9 9.6l.7-3.5L0 3.7l3.5-.4z" fill="#e7641c"/></svg><svg viewBox="0 0 10 10"><path d="M5 0l1.5 3.3 3.5.4-2.6 2.4.7 3.5L5 7.8 1.9 9.6l.7-3.5L0 3.7l3.5-.4z" fill="#e7641c"/></svg></span>
  <p>Lorem ipsum dolor sit amet, sectetur adipiscing elit. Sed fermentum fringilla ipsum ac tincidunt.</p>
  <a>Learn More</a>
</div>
<div class="card" style="left:782px">
  <div class="avatar" role="img" aria-label="Client portrait"></div>
  <span class="company">Company Name</span>
  <span class="person">Jhon Smith</span>
  <span class="stars"><svg viewBox="0 0 10 10"><path d="M5 0l1.5 3.3 3.5.4-2.6 2.4.7 3.5L5 7.8 1.9 9.6l.7-3.5L0 3.7l3.5-.4z" fill="#e7641c"/></svg><svg viewBox="0 0 10 10"><path d="M5 0l1.5 3.3 3.5.4-2.6 2.4.7 3.5L5 7.8 1.9 9.6l.7-3.5L0 3.7l3.5-.4z" fill="#e7641c"/></svg><svg viewBox="0 0 10 10"><path d="M5 0l1.5 3.3 3.5.4-2.6 2.4.7 3.5L5 7.8 1.9 9.6l.7-3.5L0 3.7l3.5-.4z" fill="#e7641c"/></svg><svg viewBox="0 0 10 10"><path d="M5 0l1.5 3.3 3.5.4-2.6 2.4.7 3.5L5 7.8 1.9 9.6l.7-3.5L0 3.7l3.5-.4z" fill="#e7641c"/></svg><svg viewBox="0 0 10 10"><path d="M5 0l1.5 3.3 3.5.4-2.6 2.4.7 3.5L5 7.8 1.9 9.6l.7-3.5L0 3.7l3.5-.4z" fill="#e7641c"/></svg></span>
  <p>Lorem ipsum dolor sit amet, sectetur adipiscing elit. Sed fermentum fringilla ipsum ac tincidunt.</p>
  <a>Learn More</a>
</div>

<!-- gallery -->
<section class="gallery">
  <h2 class="section-title" style="top:78px">OUR <span>GALLERY</span></h2>
  <div class="photo" role="img" aria-label="Long corridor with glossy blue epoxy floor" style="left:114px;top:137px;width:357px;height:415px;background:linear-gradient(180deg,#cfe3ef 0%,#6fb0d8 45%,#2f8fc7 100%)"></div>
  <div class="photo" role="img" aria-label="Outdoor stone plaza in front of office towers" style="left:481px;top:137px;width:258px;height:223px;background:linear-gradient(180deg,#8fb3d6 0%,#b8c0c6 50%,#d2d3d2 100%)"></div>
  <div class="photo" role="img" aria-label="Lobby with polished grey tile floor" style="left:481px;top:369px;width:258px;height:183px;background:linear-gradient(180deg,#4a4e55,#9aa0a6 70%,#c9ccd0)"></div>
  <div class="photo" role="img" aria-label="Floor polishing machine on a glossy floor with warm lights" style="left:748px;top:137px;width:338px;height:415px;background:linear-gradient(160deg,#d89a3a 0%,#3b3f48 40%,#8fb4d6 100%)"></div>
  <span class="btn" style="left:479px;top:582px;width:242px;height:46px">View More Projects <svg viewBox="0 0 10 10"><path d="M1 5h7M5 1l4 4-4 4" fill="none" stroke="#fff" stroke-width="2"/></svg></span>
</section>

<!-- contact -->
<h2 class="section-title" style="top:3575px">CONTACT <span>US</span></h2>
<div class="info" style="left:228px">
  <span class="ico"><svg viewBox="0 0 24 24"><path d="M6.6 10.8a15 15 0 0 0 6.6 6.6l2.2-2.2c.3-.3.7-.4 1-.2 1.1.4 2.3.6 3.6.6.6 0 1 .4 1 1V20c0 .6-.4 1-1 1A17 17 0 0 1 3 4c0-.6.4-1 1-1h3.5c.6 0 1 .4 1 1 0 1.3.2 2.5.6 3.6.1.3 0 .7-.2 1z" fill="#fff"/></svg></span>
  <div><small>Call Us Today</small><strong>+1(8888) 888 888</strong></div>
</div>
<div class="info" style="left:503px">
  <span class="ico"><svg viewBox="0 0 24 24"><rect x="3" y="5" width="18" height="14" rx="1" fill="#fff"/><path d="M3 6l9 7 9-7" fill="none" stroke="#7fa83a" stroke-width="1.8"/></svg></span>
  <div><small>Email Us Today</small><strong>info@tilebarnowl.net</strong></div>
</div>
<div class="info" style="left:778px">
  <span class="ico"><svg viewBox="0 0 24 24"><path d="M12 2a7 7 0 0 0-7 7c0 5 7 13 7 13s7-8 7-13a7 7 0 0 0-7-7z" fill="#fff"/><circle cx="12" cy="9" r="2.5" fill="#7fa83a"/></svg></span>
  <div><small>Location</small><strong>Lorum Ipsum Dolor, Texas</strong></div>
</div>
<div class="field" style="left:222px;top:3745px;width:242px;height:48px">Name</div>
<div class="field" style="left:480px;top:3745px;width:242px;height:48px">Email</div>
<div class="field" style="left:736px;top:3745px;width:242px;height:48px">Phone</div>
<div class="field" style="left:222px;top:3805px;width:756px;height:80px">Message</div>
<span class="btn" style="left:531px;top:3900px;width:136px;height:48px">Submit</span>

<!-- footer -->
<footer class="site-footer">
  <div class="brand abs" style="left:0;width:1200px;justify-content:center;top:94px;color:#fff"><i style="background:#fff"></i>tilebarnowl.net</div>
  <nav class="foot-nav"><span>HOME</span><span>ABOUT</span><span>SERVICES</span><span>GALLERY</span><span>TESTIMONIALS</span><span>CONTACT US</span></nav>
  <span class="social" style="left:533px"></span>
  <span class="social" style="left:580px"></span>
  <span class="social" style="left:627px"></span>
  <p class="copy">Copyright@2024.All Rights Reserved.</p>
</footer>

</body>
</html>
```